Brochure - Silver Harbor Circle

We need a brochure (tri-fold or bi-fold) for our network marketing company, Silver Harbor Circle. The brochure will be used for our Promoters (Distributors) to hand out to prospective customers and Promoters explaining our service as well as the income opportunity.

Industry/Entity Type

Club

```html
<!DOCTYPE html>
<html lang="en">
<head>
<meta charset="utf-8">
<title>Silver Harbor Circle – Brochure Spread</title>
<link rel="stylesheet" href="https://fonts.googleapis.com/css2?family=Open+Sans:wght@400;600;700;800&display=swap">
<style>
  :root{
    --bg:#2b2b2d;
    --paper:#ffffff;
    --paper-tint:#f1f4f7;
    --green:#7cbd3a;
    --green-dark:#5f9c25;
    --blue:#3a92e0;
    --blue-dark:#2670bd;
    --ink:#2e2e33;
    --ink-soft:#6b6f77;
    --photo-warm:#c9a98a;
    --photo-cool:#b9cbd6;
    --ui-dark:#2a2d33;
    --ui-light:#e7ecf2;
  }
  *{box-sizing:border-box;margin:0;padding:0}
  html,body{width:1200px;height:789px;overflow:hidden;background:var(--bg);font-family:"Open Sans",Arial,sans-serif;color:var(--ink)}
  .spread{position:absolute;left:30px;top:24px;width:1140px;height:741px;display:flex;box-shadow:0 10px 30px rgba(0,0,0,.5)}
  .page{position:relative;width:570px;height:741px;background:linear-gradient(160deg,var(--paper) 0%,var(--paper-tint) 100%);overflow:hidden}
  .page--left{border-right:1px solid #d8dde3}

  /* left page */
  .approach-band{position:absolute;left:150px;top:22px;right:0;height:50px;background:var(--green);color:#fff;font-weight:800;font-size:24px;letter-spacing:1px;display:flex;align-items:center;padding-left:40px}
  .step-row{position:absolute;left:0;width:570px;height:104px}
  .step-card{position:absolute;background:var(--paper);box-shadow:0 3px 8px rgba(0,0,0,.15);padding:12px 16px}
  .step-card h3{font-size:15px;font-weight:600;color:var(--ink);margin-bottom:4px}
  .step-card p{font-size:9px;line-height:1.35;color:var(--ink-soft)}
  .step-badge{position:absolute;width:46px;height:46px;background:var(--blue);color:#fff;text-align:center;font-weight:800;line-height:1;padding-top:7px;box-shadow:0 2px 5px rgba(0,0,0,.2)}
  .step-badge--green{background:var(--green)}
  .step-badge small{display:block;font-size:9px;letter-spacing:.5px}
  .step-badge span{font-size:20px}
  .media{position:absolute;box-shadow:0 2px 6px rgba(0,0,0,.2)}
  .media--ui{background:linear-gradient(180deg,var(--ui-light),#cdd6e0)}
  .media--ui-dark{background:linear-gradient(180deg,#3a3e46,var(--ui-dark))}
  .media--people{background:linear-gradient(135deg,var(--photo-warm),#8d735e)}
  .media--relax{background:linear-gradient(135deg,var(--photo-cool),#9ab97a)}
  .price-card{position:absolute;background:#fff;box-shadow:0 3px 8px rgba(0,0,0,.15);padding:10px 14px;width:150px}
  .price-card p{font-size:8.5px;color:var(--blue);line-height:1.3}
  .price-card strong{display:block;font-size:20px;color:var(--green-dark);font-weight:800;margin-top:4px}

  /* right page */
  .explainer-tab{position:absolute;left:30px;top:28px;width:220px;height:44px;background:var(--green);color:#fff;font-weight:800;font-size:22px;letter-spacing:1px;display:flex;align-items:center;padding-left:24px}
  .explainer-text{position:absolute;left:30px;top:84px;width:505px;font-size:10.5px;line-height:1.45;color:var(--ink)}
  .works-bar{position:absolute;left:30px;top:180px;width:220px;height:38px;background:var(--blue);color:#fff;font-weight:800;font-size:19px;display:flex;align-items:center;padding-left:22px}
  .works-box{position:absolute;top:232px;width:150px;height:112px;padding:34px 14px 10px;color:#fff;font-size:9px;line-height:1.35;text-align:center}
  .works-box--green{background:var(--green)}
  .works-box--blue{background:var(--blue)}
  .works-ribbon{position:absolute;left:10px;right:10px;top:8px;height:20px;font-size:10px;font-weight:700;display:flex;align-items:center;justify-content:center;color:#fff}
  .works-box--green .works-ribbon{background:var(--green-dark)}
  .works-box--blue .works-ribbon{background:var(--blue-dark)}
  .works-step{position:absolute;top:352px;width:150px;border-bottom:3px solid var(--blue);font-weight:800;font-size:15px;color:var(--ink);padding-bottom:2px;text-align:center}
  .works-step--green{border-color:var(--green)}
  .benefit-heading{position:absolute;left:30px;width:510px;font-size:14px;font-weight:700;color:var(--blue);line-height:1.3}
  .tick-list{position:absolute;left:40px;list-style:none;font-size:13px;line-height:1.55;color:var(--ink)}
  .tick-list li{display:flex;align-items:center;gap:8px}
  .tick-list svg{flex:none}
  .cta{position:absolute;left:300px;top:640px;width:210px;height:44px;background:var(--blue);color:#fff;font-weight:800;font-size:17px;display:flex;align-items:center;justify-content:center;border-radius:4px}
  .site{position:absolute;left:300px;top:696px;width:210px;font-size:14px;font-weight:600;color:var(--ink);display:flex;align-items:center;justify-content:center;gap:6px}
</style>
</head>
<body>
<main class="spread">

  <!-- Left page: step by step approach -->
  <section class="page page--left">
    <div class="approach-band">OUR UNIQUE APPROACH</div>

    <div class="step-row" style="top:84px">
      <div class="media media--ui" role="img" aria-label="Screenshot of the service category drop-down menu" style="left:30px;top:6px;width:140px;height:84px"></div>
      <div class="step-badge" style="left:196px;top:20px"><small>STEP</small><span>1</span></div>
      <div class="step-card" style="left:256px;top:10px;width:290px;box-shadow:none;background:transparent">
        <h3>Select your home service</h3>
        <p>Pick your home service need from our extensive list of categories.</p>
      </div>
    </div>

    <div class="step-row" style="top:188px">
      <div class="step-card" style="left:40px;top:8px;width:320px">
        <h3>Tell us about your project</h3>
        <p>Complete our simple questionnaire to give us an idea of what your project needs are.</p>
      </div>
      <div class="step-badge step-badge--green" style="left:380px;top:22px"><small>STEP</small><span>2</span></div>
      <div class="media media--ui" role="img" aria-label="Screenshot of the project questionnaire options" style="left:436px;top:6px;width:110px;height:88px"></div>
    </div>

    <div class="step-row" style="top:292px">
      <div class="price-card" style="left:30px;top:4px">
        <p>Thanks for that information! Based on what you've told us, the estimated price of a project like this is:</p>
        <strong>$330.00</strong>
      </div>
      <div class="step-badge" style="left:196px;top:18px"><small>STEP</small><span>3</span></div>
      <div class="step-card" style="left:256px;top:10px;width:290px;box-shadow:none;background:transparent">
        <h3>Get the average price</h3>
        <p>Based on the information provided, you'll immediately see the average price others in your area are paying for the same type of project.</p>
      </div>
    </div>

    <div class="step-row" style="top:396px">
      <div class="step-card" style="left:40px;top:6px;width:320px">
        <h3>Name your price!</h3>
        <p>Taking the average price into consideration, you now get to name your own price. Be as conservative or as bold as you wish.</p>
      </div>
      <div class="step-badge step-badge--green" style="left:380px;top:22px"><small>STEP</small><span>4</span></div>
      <div class="media media--ui-dark" role="img" aria-label="Screenshot of the name your price entry field" style="left:436px;top:6px;width:110px;height:88px"></div>
    </div>

    <div class="step-row" style="top:500px">
      <div class="media media--people" role="img" aria-label="Photo of a family of homeowners in front of their house" style="left:30px;top:4px;width:140px;height:90px"></div>
      <div class="step-badge" style="left:196px;top:20px"><small>STEP</small><span>5</span></div>
      <div class="step-card" style="left:256px;top:10px;width:290px;box-shadow:none;background:transparent">
        <h3>Your offer is distributed</h3>
        <p>We'll immediately send your price to our network of qualified, pre-screened service pros in your area.</p>
      </div>
    </div>

    <div class="step-row" style="top:606px">
      <div class="step-card" style="left:40px;top:6px;width:320px">
        <h3>Your Price is Accepted</h3>
        <p>Within 60 minutes, you will be notified when one of our service pros accepts your price. The pro will then contact you directly.</p>
      </div>
      <div class="step-badge step-badge--green" style="left:380px;top:22px"><small>STEP</small><span>6</span></div>
      <div class="media media--relax" role="img" aria-label="Photo of a relaxed homeowner on a sofa with a laptop" style="left:436px;top:6px;width:110px;height:92px"></div>
    </div>
  </section>

  <!-- Right page: explainer and promoter benefits -->
  <section class="page page--right">
    <div class="explainer-tab">EXPLAINER</div>
    <p class="explainer-text">Silver Harbor Circle's innovative model combines the bulk savings idea of Bulk Depot Club; with the "name your own price" concept of BidFare.com to fill provider vacancies. A win-win for consumers and service providers alike. Silver Harbor Circle empowers Member consumers with fair market rate information for home improvement, maintenance and repair services; and then enables them to name their own price to submit to a network of pre-screened, local service professionals who have vacancies in their schedules that they are willing to fill at the Member's submitted price.</p>

    <div class="works-bar">HOW IT WORKS</div>

    <div class="works-box works-box--green" style="left:30px">
      <div class="works-ribbon">Describe Your Need</div>
      Choose your service category and tell us about your project with just a few mouse ticks.
    </div>
    <div class="works-box works-box--blue" style="left:205px">
      <div class="works-ribbon">Name Your Price</div>
      We'll tell you the fair price for your project, then you tell us what you want to pay.
    </div>
    <div class="works-box works-box--green" style="left:380px">
      <div class="works-ribbon">Get It Done!</div>
      Within minutes, you'll receive acceptance of your project and price from one of our service professionals in your area.
    </div>
    <div class="works-step" style="left:30px">STEP 1</div>
    <div class="works-step works-step--green" style="left:205px">STEP 2</div>
    <div class="works-step" style="left:380px">STEP 3</div>

    <h2 class="benefit-heading" style="top:392px">Have A Section That Includes The Benefits Of Becoming A Silver Harbor Circle Promoter, Which Are:</h2>
    <ul class="tick-list" style="top:432px">
      <li><svg width="12" height="10" viewBox="0 0 12 10"><path d="M1 5l3.5 3.5L11 1" fill="none" stroke="#7cbd3a" stroke-width="2.4"/></svg>Earn Residual Income</li>
      <li><svg width="12" height="10" viewBox="0 0 12 10"><path d="M1 5l3.5 3.5L11 1" fill="none" stroke="#7cbd3a" stroke-width="2.4"/></svg>Reclaim Your Time</li>
      <li><svg width="12" height="10" viewBox="0 0 12 10"><path d="M1 5l3.5 3.5L11 1" fill="none" stroke="#7cbd3a" stroke-width="2.4"/></svg>Help People Save Money</li>
    </ul>

    <h2 class="benefit-heading" style="top:508px">Have A Section That Includes What's Included When Becoming A Silver Harbor Circle Promoter, Which Are:</h2>
    <ul class="tick-list" style="top:548px;font-size:12px;line-height:1.45">
      <li><svg width="12" height="10" viewBox="0 0 12 10"><path d="M1 5l3.5 3.5L11 1" fill="none" stroke="#7cbd3a" stroke-width="2.4"/></svg>Personalized Replicated Website</li>
      <li><svg width="12" height="10" viewBox="0 0 12 10"><path d="M1 5l3.5 3.5L11 1" fill="none" stroke="#7cbd3a" stroke-width="2.4"/></svg>Back-office Suite</li>
      <li><svg width="12" height="10" viewBox="0 0 12 10"><path d="M1 5l3.5 3.5L11 1" fill="none" stroke="#7cbd3a" stroke-width="2.4"/></svg>Personal Earnings Report</li>
      <li><svg width="12" height="10" viewBox="0 0 12 10"><path d="M1 5l3.5 3.5L11 1" fill="none" stroke="#7cbd3a" stroke-width="2.4"/></svg>Marketing Tools</li>
      <li><svg width="12" height="10" viewBox="0 0 12 10"><path d="M1 5l3.5 3.5L11 1" fill="none" stroke="#7cbd3a" stroke-width="2.4"/></svg>Team Telemetry</li>
      <li><svg width="12" height="10" viewBox="0 0 12 10"><path d="M1 5l3.5 3.5L11 1" fill="none" stroke="#7cbd3a" stroke-width="2.4"/></svg>Sales Training</li>
      <li><svg width="12" height="10" viewBox="0 0 12 10"><path d="M1 5l3.5 3.5L11 1" fill="none" stroke="#7cbd3a" stroke-width="2.4"/></svg>Technical Support</li>
    </ul>

    <div class="cta">GET STARTED NOW!</div>
    <div class="site">
      <svg width="14" height="14" viewBox="0 0 14 14"><circle cx="7" cy="7" r="6" fill="none" stroke="#2e2e33" stroke-width="1.3"/><path d="M1 7h12M7 1c-3 3-3 9 0 12M7 1c3 3 3 9 0 12" fill="none" stroke="#2e2e33" stroke-width="1"/></svg>
      www.shcircle.com
    </div>
  </section>

</main>
</body>
</html>
```